Priority Goals poster for school year

We are an elementary school and the past two years have had you help us to design a "poster" that illustrates our goal of the coming year. I am attaching our last year's one, along with some photos of our (ver rough) thinking for next years. The priority goal at top remains the same. Can't wait to see your genius ideas! :)

Target Market(s)

Staff of an elementary school and parents to some (informative) extent as well.

Colors
296eb1
6094c6
fbed22
fbee3f

Requirements
Must have
• items from the white board picture we have attached

```html
<!DOCTYPE html>
<html lang="en">
<head>
<meta charset="utf-8">
<title>2021-22 Priority Goals – Cedar Ridge Elementary School</title>
<link href="https://fonts.googleapis.com/css2?family=Montserrat:wght@400;500;600;700;800&display=swap" rel="stylesheet">
<style>
  :root {
    --navy: #2b4596;
    --gold: #e9c636;
    --gold-ring: #f0cc1e;
    --white: #ffffff;
    --mist: #eceef3;
    --heart-edge: #e1e2e6;
  }
  html, body {
    margin: 0;
    padding: 0;
    overflow: hidden;
    background: var(--white);
  }
  .poster {
    position: relative;
    width: 848px;
    height: 1200px;
    overflow: hidden;
    background: var(--white);
    font-family: "Montserrat", sans-serif;
    color: var(--navy);
  }
  .poster svg { display: block; }
  .goal-text { font-family: "Montserrat", sans-serif; font-weight: 500; }
  .goal-text.on-gold { fill: var(--navy); }
  .goal-text.on-navy { fill: var(--white); }
  .goal-text.title { font-weight: 700; }
  .headline { font-family: "Montserrat", sans-serif; font-weight: 800; }
  .footer-text { font-family: "Montserrat", sans-serif; font-weight: 700; fill: var(--white); }
</style>
</head>
<body>
<div class="poster">
<svg width="848" height="1200" viewBox="0 0 848 1200" xmlns="http://www.w3.org/2000/svg">
  <defs>
    <linearGradient id="backdropFade" x1="0" y1="0" x2="0" y2="1">
      <stop offset="0" stop-color="#ffffff"/>
      <stop offset="0.15" stop-color="#eef0f5"/>
      <stop offset="0.85" stop-color="#eef0f5"/>
      <stop offset="1" stop-color="#ffffff"/>
    </linearGradient>
    <linearGradient id="mascotTone" x1="0" y1="0" x2="1" y2="1">
      <stop offset="0" stop-color="#e9c636"/>
      <stop offset="1" stop-color="#4a63b0"/>
    </linearGradient>
    <path id="wheelBlade" d="M0,0 Q132,-145 327,-135.5 A354,354 0 0 1 327,135.5 Q196,-8.5 0,0 Z"/>
  </defs>

  <!-- faint mascot backdrop -->
  <rect class="backdrop-art" x="0" y="215" width="848" height="790" fill="url(#backdropFade)"
        role="img" aria-label="Faint school mascot and math sketches in the background"/>

  <!-- headline -->
  <text class="headline" x="320" y="71" font-size="66" fill="var(--navy)" text-anchor="middle" letter-spacing="-1">2021-22</text>
  <rect class="title-band" x="0" y="77" width="830" height="65" fill="var(--navy)"/>
  <text class="headline" x="18" y="134" font-size="62" fill="var(--white)" letter-spacing="0.5">PRIORITY GOALS</text>
  <rect class="intro-band" x="0" y="142" width="620" height="65" fill="var(--gold)"/>
  <text class="goal-text on-gold" x="20" y="170" font-size="20">We will accelerate the academic &amp; Social/Emotional</text>
  <text class="goal-text on-gold" x="20" y="194" font-size="20">Growth of the students we serve by:</text>

  <!-- school mark -->
  <rect class="school-mark" x="598" y="22" width="240" height="230" fill="var(--white)"/>
  <text class="headline" x="718" y="86" font-size="60" fill="var(--navy)" text-anchor="middle">CRES</text>
  <rect class="mascot-art" x="602" y="76" width="226" height="118" rx="30" fill="url(#mascotTone)"
        role="img" aria-label="School mascot illustration"/>
  <text class="headline" x="718" y="221" font-size="27" fill="var(--navy)" text-anchor="middle">CEDAR RIDGE</text>
  <text class="headline" x="718" y="244" font-size="18" fill="var(--navy)" text-anchor="middle">ELEMENTARY SCHOOL</text>

  <!-- goal wheel -->
  <g class="goal-wheel">
    <circle cx="423" cy="608" r="372" fill="var(--white)" stroke="var(--gold-ring)" stroke-width="8"/>
    <circle cx="423" cy="608" r="354" fill="var(--gold)"/>
    <g transform="translate(423 608)" fill="var(--navy)">
      <use href="#wheelBlade" transform="rotate(-70)"/>
      <use href="#wheelBlade" transform="rotate(20)"/>
      <use href="#wheelBlade" transform="rotate(110)"/>
      <use href="#wheelBlade" transform="rotate(200)"/>
    </g>
  </g>

  <!-- heart -->
  <path class="heart" d="M422,530 C395,502 345,498 305,510 C275,525 278,575 300,610 C330,660 390,705 422,738 C454,705 514,660 544,610 C566,575 569,525 539,510 C499,498 449,502 422,530 Z"
        fill="var(--white)" stroke="var(--heart-edge)" stroke-width="6" stroke-linejoin="round"/>
  <rect class="graduate-icon" x="350" y="410" width="138" height="100" rx="20" fill="#ffffff" opacity="0.9"
        role="img" aria-label="Graduate cap icon"/>
  <rect class="school-icons" x="315" y="530" width="215" height="145" rx="18" fill="#dfe4f1"
        role="img" aria-label="Teacher, team and school building icons"/>

  <!-- goals -->
  <g class="goal-text on-gold" font-size="18">
    <text x="217" y="365">Voices of All</text>
    <text x="217" y="392">Who are we?</text>
    <text x="217" y="420">Where are we</text>
    <text x="217" y="442">going?</text>
  </g>
  <text class="goal-text on-navy" x="403" y="352" font-size="18">Broaden our Lead</text>
  <g class="goal-text on-gold" font-size="18">
    <text x="556" y="450">Staff doing what</text>
    <text x="556" y="472">they Love...</text>
    <text x="557" y="504">Teaching kids for</text>
    <text x="557" y="526">Proven Growth</text>
  </g>
  <g class="goal-text on-navy" font-size="18">
    <text x="583" y="590">Communicate,</text>
    <text x="583" y="613">Communicate,</text>
    <text x="583" y="637">Communicate,</text>
  </g>
  <g class="goal-text on-navy" font-size="16" fill="var(--white)">
    <circle cx="609" cy="659" r="4.5"/><text x="621" y="664">Expectations</text>
    <circle cx="623" cy="685" r="4.5"/><text x="638" y="690">Support</text>
    <circle cx="636" cy="710" r="4.5"/><text x="648" y="716">For Clarity</text>
  </g>
  <g class="goal-text on-gold title" font-size="19">
    <text x="483" y="748">Build Value</text>
    <text x="483" y="771">Partnership</text>
  </g>
  <g class="goal-text on-gold" font-size="16" fill="var(--navy)">
    <circle cx="487" cy="787" r="4.5"/><text x="497" y="792">Correct</text>
    <circle cx="487" cy="810" r="4.5"/><text x="497" y="815">Celebrate</text>
    <circle cx="487" cy="833" r="4.5"/><text x="497" y="838">Strong, Predictable</text>
    <circle cx="487" cy="858" r="4.5"/><text x="497" y="863">Laugh,Have Fun</text>
  </g>
  <text class="goal-text on-navy title" x="305" y="822" font-size="18">Wellness</text>
  <g class="goal-text on-navy" font-size="16">
    <text x="272" y="849">Mental Health for every</text>
    <text x="272" y="871">person in our school</text>
    <text x="272" y="893">community</text>
  </g>
  <g class="goal-text on-gold" font-size="19">
    <text x="126" y="726">Be intentional with</text>
    <text x="126" y="749">each action- Focus</text>
  </g>
  <g class="goal-text on-navy" font-size="18">
    <text x="115" y="546">Small Measured</text>
    <text x="116" y="573">Step Towards</text>
    <text x="117" y="599">Larger Goal</text>
  </g>

  <!-- foundational promises -->
  <text class="headline" x="424" y="1045" font-size="54" fill="var(--navy)" text-anchor="middle" letter-spacing="-0.5">FOUNDATIONAL PROMISES</text>
  <text class="goal-text" x="424" y="1083" font-size="29" fill="var(--navy)" text-anchor="middle">( 4 YEARS STRONG, BETTER EVERYDAY )</text>

  <!-- footer -->
  <rect class="footer-accent" x="0" y="1100" width="848" height="13" fill="var(--gold)"/>
  <rect class="footer" x="0" y="1113" width="848" height="87" fill="var(--navy)"/>
  <path class="pin-icon" d="M41,1150 C34,1141 31,1137 31,1132 A10,10 0 0 1 51,1132 C51,1137 48,1141 41,1150 Z M41,1128 A4,4 0 1 0 41,1136 A4,4 0 1 0 41,1128 Z"
        fill="var(--white)" fill-rule="evenodd"/>
  <text class="footer-text" x="60" y="1148" font-size="19">1870 Birchwood Ave., Pine Hollow, WA 98200</text>
  <path class="phone-icon" d="M37,1167 q-5,3 -3,11 q3,9 10,12 q5,2 7,-2 l-4,-5 q-2,1 -4,0 q-3,-3 -3,-7 q1,-2 3,-2 z" fill="var(--white)"/>
  <text class="footer-text" x="58" y="1190" font-size="29">555-014-2780</text>
  <rect class="social-mark" x="582" y="1143" width="32" height="32" rx="8" fill="var(--white)"/>
  <text class="footer-text" x="623" y="1165" font-size="18" font-weight="500">@cedarridgelearners</text>
</svg>
</div>
</body>
</html>
```